New Website for NY and South Florida Based Accounting Firm

Accounting and Audit firm located in New York and South Florida needs a website redesign after acquiring new businesses and adding new services.

Our current website can be found here:
http://www.tkrbwco.example/

We have merged with this firm:
http://halloranbeckwithstrand.example/

We are looking for a comprehensive design that will highlight the firm's dual locations. The final design should communicate security, strength, and growth. We would like to keep our pyramid logo as seen on the tkrbwco.example website, as this has been our logo for over 20 years.

Industry/Entity Type

Accounting

Number of Pages Required

1 page

Font styles to use
Serif
Sans Serif

```html
<!DOCTYPE html>
<html lang="en">
<head>
<meta charset="utf-8">
<title>Thackeray, Keene, Rowan &amp; Brill, LLP</title>
<link href="https://fonts.googleapis.com/css2?family=Montserrat:wght@400;600;700;800&family=Open+Sans:wght@400;600;700&display=swap" rel="stylesheet">
<style>
:root{
  --orange:#f39a1f;
  --orange-dark:#d9820c;
  --ink:#222326;
  --text:#4a4a4a;
  --muted:#8a8a8a;
  --grey-bg:#ededed;
  --white:#ffffff;
  --footer-bar:#2b2b2b;
}
*{box-sizing:border-box;margin:0;padding:0}
html,body{width:1200px;height:2448px;overflow:hidden}
body{font-family:"Open Sans",Arial,sans-serif;color:var(--text);background:var(--white);position:relative}
.heading{font-family:"Montserrat",Arial,sans-serif}

/* header */
.site-header{position:absolute;top:0;left:0;width:1200px;height:128px;background:var(--white);z-index:2}
.brand{position:absolute;left:100px;top:26px;display:flex;align-items:center;gap:12px}
.brand-mark{width:26px;height:26px;background:var(--orange)}
.brand-name{font-family:"Montserrat",sans-serif;font-weight:800;font-size:30px;color:var(--ink);letter-spacing:2px}
.header-panel{position:absolute;right:0;top:0;width:620px;height:128px;background:var(--orange)}
.contact-row{height:62px;display:flex;align-items:center;justify-content:flex-end;padding-right:40px;gap:14px;color:var(--white);font-weight:700;font-size:20px}
.social{display:flex;gap:6px}
.social span{width:20px;height:20px;border-radius:50%;background:var(--white);opacity:.9}
.main-nav{height:50px;display:flex;align-items:center;padding-left:20px;gap:26px;font-family:"Montserrat",sans-serif;font-size:13px;font-weight:600;color:var(--white);background:var(--orange-dark)}
.nav-buttons{margin-left:auto;margin-right:30px;display:flex;gap:6px}
.nav-buttons span{background:var(--ink);padding:6px 12px;font-size:11px}
.nav-buttons span+span{background:var(--white);color:var(--ink)}

/* hero */
.hero{position:absolute;top:128px;left:0;width:1200px;height:532px;background:linear-gradient(180deg,#c9d6e3 0%,#9aa5ae 35%,#6b5a48 75%,#4d3c2c 100%)}
.hero-banner{position:absolute;left:60px;top:230px;background:rgba(243,154,31,.88);padding:16px 26px;font-family:"Montserrat",sans-serif;font-weight:700;font-size:28px;color:var(--white);letter-spacing:1px}

/* why */
.why{position:absolute;top:660px;left:0;width:1200px;height:420px;text-align:center}
.section-title{font-family:"Montserrat",sans-serif;font-weight:800;font-size:36px;color:var(--ink);letter-spacing:1px;padding-top:56px}
.title-rule{width:60px;height:4px;background:var(--orange);margin:12px auto 0}
.why-text{width:980px;margin:24px auto 0;font-size:15px;line-height:24px}
.why-cards{display:flex;gap:14px;justify-content:center;margin-top:30px}
.why-card{width:256px}
.why-photo{height:126px}
.why-label{height:38px;background:var(--orange);display:flex;align-items:center;justify-content:space-between;padding:0 14px 0 20px;font-family:"Montserrat",sans-serif;font-weight:700;font-size:14px;color:var(--white)}
.arrow{width:24px;height:24px;border-radius:50%;background:var(--ink);display:flex;align-items:center;justify-content:center}

/* offer */
.offer{position:absolute;top:1080px;left:0;width:1200px;height:720px;background:var(--grey-bg)}
.offer .section-title{text-align:center;padding-top:50px}
.person-photo{position:absolute;left:100px;top:165px;width:350px;height:555px;background:linear-gradient(180deg,#e2e2e2 0%,#a7a9ad 40%,#55595f 100%)}
.service-grid{position:absolute;left:480px;top:200px;display:grid;grid-template-columns:repeat(3,208px);gap:20px 18px}
.service-card{background:var(--white);height:210px;text-align:center;padding-top:20px}
.service-card svg{display:block;margin:0 auto}
.service-kicker{font-size:11px;color:var(--orange);margin-top:8px}
.service-name{font-family:"Montserrat",sans-serif;font-weight:700;font-size:16px;color:var(--ink);margin-top:2px}
.service-desc{font-size:11px;color:var(--muted);margin:8px 18px 0;line-height:15px}
.read-more{display:inline-block;margin-top:12px;background:var(--ink);color:var(--white);font-family:"Montserrat",sans-serif;font-weight:700;font-size:11px;padding:8px 16px}

/* reviews */
.reviews{position:absolute;top:1800px;left:0;width:1200px;height:445px;background:linear-gradient(180deg,#2c2c2e 0%,#3e3a35 60%,#2a2a2a 100%);text-align:center;color:var(--white)}
.reviews-kicker{padding-top:36px;font-size:16px}
.reviews .section-title{color:var(--white);padding-top:6px;font-size:34px}
.reviews-text{width:1000px;margin:26px auto 0;font-size:14px;line-height:22px;color:#d8d8d8;text-align:left}
.reviewer{display:flex;justify-content:center;align-items:center;gap:18px;margin-top:34px}
.reviewer-photo{width:80px;height:80px;background:linear-gradient(180deg,#c9b7a4,#7d6a58)}
.reviewer-name{font-family:"Montserrat",sans-serif;font-weight:700;font-size:16px;text-align:left}
.reviewer-role{font-size:12px;color:var(--orange);text-align:left}

/* footer */
.site-footer{position:absolute;top:2245px;left:0;width:1200px;height:165px;background:var(--orange);display:grid;grid-template-columns:400px 230px 200px 220px;gap:20px;padding:24px 60px 0 100px;color:var(--white)}
.footer-brand{display:flex;gap:10px;align-items:center}
.footer-brand .brand-mark{background:var(--white);width:20px;height:20px}
.footer-brand-name{font-family:"Montserrat",sans-serif;font-weight:800;font-size:18px;line-height:22px;color:var(--ink)}
.footer-about{font-size:11px;line-height:16px;margin-top:10px}
.footer-title{font-family:"Montserrat",sans-serif;font-weight:700;font-size:22px;letter-spacing:1px;margin-bottom:8px}
.footer-col p,.footer-col li{font-size:11px;line-height:16px;list-style:none}
.footer-social{display:flex;gap:5px;margin-top:8px}
.footer-social span{width:18px;height:18px;border-radius:50%;background:var(--ink)}
.copyright{position:absolute;top:2410px;left:0;width:1200px;height:38px;background:var(--footer-bar);color:#bbb;font-size:11px;text-align:center;line-height:38px;letter-spacing:1px}
</style>
</head>
<body>

<header class="site-header">
  <div class="brand"><span class="brand-mark"></span><span class="brand-name">TKRB</span></div>
  <div class="header-panel">
    <div class="contact-row">
      <svg width="20" height="20" viewBox="0 0 24 24"><path fill="#fff" d="M6.6 10.8a15 15 0 0 0 6.6 6.6l2.2-2.2c.3-.3.7-.4 1-.2 1.1.4 2.3.6 3.6.6.6 0 1 .4 1 1V20c0 .6-.4 1-1 1A17 17 0 0 1 3 4c0-.6.4-1 1-1h3.5c.6 0 1 .4 1 1 0 1.3.2 2.5.6 3.6.1.3 0 .7-.2 1z"/></svg>
      <span>555-014-2200</span>
      <div class="social"><span></span><span></span><span></span><span></span></div>
    </div>
    <nav class="main-nav">
      <span>HOME</span><span>WHY TKRB</span><span>SERVICES</span><span>PROFILES</span><span>TIPS &amp; LINKS</span><span>CONTACT</span>
      <div class="nav-buttons"><span>LOGIN</span><span>SIGNUP</span></div>
    </nav>
  </div>
</header>

<section class="hero" role="img" aria-label="Aerial photograph of a city skyline with skyscrapers at sunset">
  <div class="hero-banner">SIMPLY DUMMY TEXT OF THE PRINTING</div>
</section>

<section class="why">
  <h2 class="section-title">WHY TKRB</h2>
  <div class="title-rule"></div>
  <p class="why-text">Thackeray, Keene, Rowan &amp; Brill, LLP is an accounting, audit and business management firm with offices in New York City, Long Island, and Florida. Our experienced CPA's offer financial solutions and cost resources in all aspects accounting.</p>
  <div class="why-cards">
    <div class="why-card"><div class="why-photo" role="img" aria-label="Photo of business people shaking hands" style="background:linear-gradient(135deg,#cdb89d,#6f5c48)"></div><div class="why-label">ABOUT TKRB<span class="arrow"><svg width="10" height="10" viewBox="0 0 10 10"><path d="M3 1l4 4-4 4" stroke="#fff" stroke-width="2" fill="none"/></svg></span></div></div>
    <div class="why-card"><div class="why-photo" role="img" aria-label="Photo of a desk with tablet, coffee and notes" style="background:linear-gradient(135deg,#d9dde2,#7f8891)"></div><div class="why-label">PROFILES<span class="arrow"><svg width="10" height="10" viewBox="0 0 10 10"><path d="M3 1l4 4-4 4" stroke="#fff" stroke-width="2" fill="none"/></svg></span></div></div>
    <div class="why-card"><div class="why-photo" role="img" aria-label="Photo of hands working on financial charts" style="background:linear-gradient(135deg,#e4e6ea,#8d959f)"></div><div class="why-label">TIPS AND LINKS<span class="arrow"><svg width="10" height="10" viewBox="0 0 10 10"><path d="M3 1l4 4-4 4" stroke="#fff" stroke-width="2" fill="none"/></svg></span></div></div>
    <div class="why-card"><div class="why-photo" role="img" aria-label="Photo of a calculator and pen on documents" style="background:linear-gradient(135deg,#c8ccd2,#5e646c)"></div><div class="why-label">CAREER<span class="arrow"><svg width="10" height="10" viewBox="0 0 10 10"><path d="M3 1l4 4-4 4" stroke="#fff" stroke-width="2" fill="none"/></svg></span></div></div>
  </div>
</section>

<section class="offer">
  <h2 class="section-title">WE OFFER YOU</h2>
  <div class="title-rule"></div>
  <div class="person-photo" role="img" aria-label="Photo of a smiling businessman in a grey suit"></div>
  <div class="service-grid">
    <div class="service-card">
      <svg width="34" height="34" viewBox="0 0 34 34"><rect x="7" y="3" width="20" height="28" rx="2" fill="#555"/><rect x="10" y="6" width="14" height="6" fill="#fff"/><g fill="#fff"><rect x="10" y="15" width="4" height="3"/><rect x="15" y="15" width="4" height="3"/><rect x="20" y="15" width="4" height="3"/><rect x="10" y="21" width="4" height="3"/><rect x="15" y="21" width="4" height="3"/><rect x="20" y="21" width="4" height="8"/><rect x="10" y="26" width="9" height="3"/></g></svg>
      <p class="service-kicker">Many Years Of Experience</p><h3 class="service-name">ACCOUNTING</h3>
      <p class="service-desc">Clear reporting for every client need.</p><span class="read-more">READ MORE</span>
    </div>
    <div class="service-card">
      <svg width="34" height="34" viewBox="0 0 34 34"><circle cx="14" cy="14" r="9" fill="none" stroke="#555" stroke-width="4"/><path d="M21 21l9 9" stroke="#555" stroke-width="5" stroke-linecap="round"/></svg>
      <p class="service-kicker">Many Years Of Experience</p><h3 class="service-name">AUDITING</h3>
      <p class="service-desc">Careful reviews that build lasting trust.</p><span class="read-more">READ MORE</span>
    </div>
    <div class="service-card">
      <svg width="34" height="34" viewBox="0 0 34 34"><path d="M8 3h14l6 6v22H8z" fill="#555"/><path d="M12 14h12M12 19h12M12 24h8" stroke="#fff" stroke-width="2"/></svg>
      <p class="service-kicker">Many Years Of Experience</p><h3 class="service-name">TAX SERVICES</h3>
      <p class="service-desc">Smart planning for individuals and firms.</p><span class="read-more">READ MORE</span>
    </div>
    <div class="service-card">
      <svg width="34" height="34" viewBox="0 0 34 34"><g fill="#555"><circle cx="17" cy="10" r="5"/><path d="M9 28c0-6 3.5-9 8-9s8 3 8 9z"/><circle cx="7" cy="13" r="3.5"/><path d="M1 27c0-4 2.5-7 6-7 1.5 0 2 .3 2.5.6C8 22 7.5 24 7.5 27z"/><circle cx="27" cy="13" r="3.5"/><path d="M33 27c0-4-2.5-7-6-7-1.5 0-2 .3-2.5.6 1.5 1.4 2 3.4 2 6.4z"/></g></svg>
      <p class="service-kicker">Many Years Of Experience</p><h3 class="service-name">MANAGEMENT</h3>
      <p class="service-desc">Guidance that keeps your business moving.</p><span class="read-more">READ MORE</span>
    </div>
    <div class="service-card">
      <svg width="34" height="34" viewBox="0 0 34 34"><g fill="#555"><rect x="4" y="20" width="6" height="11"/><rect x="14" y="13" width="6" height="18"/><rect x="24" y="6" width="6" height="25"/></g></svg>
      <p class="service-kicker">Many Years Of Experience</p><h3 class="service-name">FINANCIAL</h3>
      <p class="service-desc">Sound advice for steady long growth.</p><span class="read-more">READ MORE</span>
    </div>
    <div class="service-card">
      <svg width="34" height="34" viewBox="0 0 34 34"><circle cx="17" cy="13" r="9" fill="#555"/><rect x="13" y="23" width="8" height="6" fill="#555"/><rect x="14" y="30" width="6" height="2" fill="#555"/></svg>
      <p class="service-kicker">Many Years Of Experience</p><h3 class="service-name">TIPS &amp; LINKS</h3>
      <p class="service-desc">Useful resources to help you plan.</p><span class="read-more">READ MORE</span>
    </div>
  </div>
</section>

<section class="reviews" role="img" aria-label="Dimmed photo of a city skyline behind customer reviews">
  <p class="reviews-kicker">Want To Know About Customers Thinking</p>
  <h2 class="section-title">CUSTOMER REVIEWS</h2>
  <p class="reviews-text">Working with this team has made our year end close calmer and faster. They explain every figure in plain terms, answer calls the same day, and always look for ways to save us money. Our books have never been cleaner, and our audits now run smoothly from start to finish. We trust them with our growth plans and recommend them to every business owner we know.</p>
  <div class="reviewer">
    <div class="reviewer-photo" role="img" aria-label="Portrait photo of the reviewer"></div>
    <div><p class="reviewer-name">DALE MORROW</p><p class="reviewer-role">Chief Financial Officer</p></div>
  </div>
</section>

<footer class="site-footer">
  <div class="footer-col">
    <div class="footer-brand"><span class="brand-mark"></span><span class="footer-brand-name">THACKERAY, KEENE<br>ROWAN &amp; BRILL</span></div>
    <p class="footer-about">We have established a strong reputation as a firm of highly skilled experts providing experienced and attentive audit services to our clients.</p>
  </div>
  <div class="footer-col">
    <h3 class="footer-title">ADDRESS</h3>
    <p>1250 Harbor Park Drive, Suite 200<br>Melville, NY 11747</p><br>
    <p>400 Coral Way, Suite 12<br>Boca Raton, FL 33431</p>
  </div>
  <div class="footer-col">
    <h3 class="footer-title">ABOUT US</h3>
    <ul><li>› HOME</li><li>› WHY TKRB</li><li>› SERVICES</li><li>› PROFILES</li><li>› TIPS &amp; LINKS</li></ul>
  </div>
  <div class="footer-col">
    <h3 class="footer-title">CONTACT US</h3>
    <p>Phone: 555-014-2200<br>Fax: 555-014-2201<br>info@tkrbwco.example</p>
    <div class="footer-social"><span></span><span></span><span></span><span></span><span></span><span></span></div>
  </div>
</footer>
<div class="copyright">Copyright © 2024 tkrbwco.example. All rights reserved.</div>

</body>
</html>
```